Corrabeen Holiday Village Flyer Project

Flyer required for a holiday caravan park. I have attached the current flyer for the park and would like to use the same layout. Please also alter the changes to the text that I have marked up. Until the additional uploads for the new images are ready, could you please just leave those as a blank square and the images can be inserted once I have them loaded.

Target Market(s)

Holiday makers

Industry/Entity Type

Tourism

Colors
3176b5
33a6d7
0393ce
fbee3e
fbed22
ffffff
faa54b

Requirements
Must have
• copy the attached flyer
• Would like a better title font for the front text - "Corrabeen Holiday Village", please make that a more playful holiday feel font
• Please use images 001 & 002 as the front cover images
• I have more images to load up which will be done 4/7.
Nice to have
• would like a better colour back ground to the flyer, maybe blue-ish and then alter the colour of the text accordingly
Should not have
• Please use the attached flyer copy as a template

```html
<!DOCTYPE html>
<html lang="en">
<head>
<meta charset="utf-8">
<title>Corrabeen Holiday Village – Trifold Flyer</title>
<link href="https://fonts.googleapis.com/css2?family=Fredoka:wght@600&family=Poppins:wght@300;400;500;600&family=Fjalla+One&display=swap" rel="stylesheet">
<style>
  :root{
    --stage:#3b3b3b;
    --navy:#1d4f8a;
    --blue:#3176b5;
    --sky:#33a6d7;
    --cyan:#0393ce;
    --ink:#14324f;
    --pale:#eaf6fb;
    --band:#6cc8de;
    --white:#ffffff;
  }
  *{box-sizing:border-box;margin:0;padding:0}
  html,body{width:784px;height:1200px;overflow:hidden;background:var(--stage)}
  body{position:relative;font-family:"Poppins",sans-serif;color:var(--ink)}
  .spread{position:absolute;left:6px;width:772px;height:580px;overflow:hidden;
    box-shadow:0 2px 6px rgba(0,0,0,.5)}
  .spread--outside{top:8px}
  .spread--inside{top:604px}
  .panel{position:absolute;top:0;height:580px;overflow:hidden}
  .panel--left{left:0;width:248px}
  .panel--mid{left:248px;width:264px}
  .panel--right{left:512px;width:260px}
  .abs{position:absolute}

  .bg-light{background:linear-gradient(180deg,#f4fbfe 0%,#e3f3fa 60%,#d3edf7 100%)}
  .bg-cover-mid{background:linear-gradient(180deg,#f3fafd 0%,#e1f2fa 55%,#8fd0ec 72%,#7cc6e8 100%)}
  .bg-cover-right{background:linear-gradient(180deg,#9bd5ee 60%,#8accea 100%)}

  .band{position:absolute;left:0;height:23px;
    background:linear-gradient(90deg,#5cc2da 0%,#8fd6e6 60%,rgba(200,236,245,.2) 100%);
    font-family:"Fjalla One",sans-serif;color:var(--ink);font-size:18px;line-height:23px;padding-left:30px;letter-spacing:.2px}
  .band--small{font-size:13px;padding-left:22px;height:22px;line-height:22px}

  .title{font-family:"Fredoka",sans-serif;font-weight:600;letter-spacing:1.5px;line-height:1}
  .subtitle{font-weight:400;letter-spacing:3px;line-height:1}

  .intro{left:18px;top:222px;width:212px;font-size:9.4px;line-height:14.6px;color:var(--navy);font-weight:500;text-align:justify}
  .activity-col{list-style:none;font-size:8.6px;font-weight:500;text-transform:uppercase;color:var(--ink)}
  .activity-col li{margin-bottom:7px;line-height:1.15}
  .activity-col--right li{margin-bottom:9.6px;line-height:1}
  .divider{position:absolute;width:1.5px;background:var(--blue)}

  .attractions{left:0;top:484px;width:248px;height:82px;
    background:linear-gradient(90deg,#55bfd8 0%,#9adbea 70%,rgba(220,244,250,.4) 100%);
    font-family:"Fjalla One",sans-serif;font-size:17px;line-height:20px;text-align:center;padding-top:12px;color:var(--ink)}

  .contact{list-style:none;font-size:10.8px;letter-spacing:.3px;color:var(--ink)}
  .contact li{display:flex;align-items:center;height:17px;white-space:nowrap}
  .contact li.web{margin-top:16px;font-size:12px}
  .icon{width:11px;height:11px;margin-right:9px;flex:none}

  .photo{position:absolute}

  .sub-head{font-size:11.5px;color:var(--blue);font-weight:400;line-height:14px}
  .pair{display:grid;grid-template-columns:125px 100px;font-size:9.6px;text-transform:uppercase;line-height:13px;color:var(--ink)}

  .plain-list{list-style:none;font-size:11.4px;line-height:22.6px;color:var(--ink)}
  .caps-list{list-style:none;font-size:9.6px;font-weight:500;text-transform:uppercase;color:var(--blue);line-height:17.6px;white-space:nowrap}
  .footer-box{left:0;top:516px;width:260px;height:64px;background:#dceef8;padding:10px 0 0 8px;font-size:10px;line-height:15px}
  .footer-line{display:flex;align-items:center;gap:5px;margin-top:8px;font-size:8.8px;white-space:nowrap}
</style>
</head>
<body>

<section class="spread spread--outside">

  <div class="panel panel--left bg-light">
    <svg class="abs" style="left:0;top:0" width="248" height="215" role="img" aria-label="Location map showing the village between the beach and the estuary">
      <defs>
        <linearGradient id="mapFill" x1="0" y1="0" x2="1" y2="1">
          <stop offset="0" stop-color="#a7d86a"/><stop offset=".55" stop-color="#8fd0a0"/><stop offset="1" stop-color="#45b7d6"/>
        </linearGradient>
      </defs>
      <circle cx="116" cy="88" r="126" fill="url(#mapFill)" stroke="#1e62a8" stroke-width="3"/>
    </svg>
    <p class="abs intro">We are the second turn to left, after the bridge. Ideally located nestled between Melrose Beach and the Estuary, 3-minutes south of the Corrabeen cut with all the associated water activities and 15-minutes from Mandurah CBD boasting.</p>

    <div class="band band--small" style="top:326px">A RANGE OF ACTIVITIES SUCH AS</div>
    <ul class="abs activity-col" style="left:18px;top:363px;width:124px">
      <li>Summer Concerts</li><li>Dolphin Tours</li><li>Movie Theatres</li><li>Suberb Restaurants</li><li>Seaside Markets</li><li>Harbourside Performing Arts Centre</li>
    </ul>
    <span class="divider" style="left:145px;top:360px;height:108px"></span>
    <ul class="abs activity-col activity-col--right" style="left:156px;top:363px;width:88px">
      <li>Wineries</li><li>Wildlife Parks</li><li>Taverns</li><li>Night Clubs</li><li>Festivals</li><li>Art Gallery</li>
    </ul>
    <div class="abs attractions">HISTORICAL SITES AND<br>MANY MORE TOURIST<br>ATTRACTIONS!</div>
  </div>

  <div class="panel panel--mid bg-cover-mid">
    <svg class="abs" style="left:0;top:300px" width="264" height="90" viewBox="0 0 264 90">
      <path d="M0 12 C80 -2 170 10 264 55 L264 90 L0 90 Z" fill="#8dcfec" opacity=".6"/>
      <path d="M0 10 C90 0 180 18 264 58" fill="none" stroke="#3b8fd0" stroke-width="2"/>
    </svg>
    <div class="abs title" style="left:0;width:264px;top:194px;text-align:center;font-size:36px;color:var(--navy)">CORRABEEN</div>
    <div class="abs subtitle" style="left:0;width:264px;top:234px;text-align:center;font-size:16px;color:var(--ink)">HOLIDAY VILLAGE</div>
    <ul class="abs contact" style="left:22px;top:362px">
      <li><svg class="icon" viewBox="0 0 12 12"><circle cx="6" cy="6" r="6" fill="var(--blue)"/><path d="M3.6 3.2l1.2-.4.8 1.6-.7.6c.4.9 1 1.5 1.9 1.9l.6-.7 1.6.8-.4 1.2C5.8 8.4 3.6 6.2 3.6 3.2z" fill="#fff"/></svg>(08) 9477 2305</li>
      <li><svg class="icon" viewBox="0 0 12 12"><path d="M6 0.5a4 4 0 0 1 4 4c0 3-4 7-4 7s-4-4-4-7a4 4 0 0 1 4-4z" fill="var(--blue)"/><circle cx="6" cy="4.5" r="1.6" fill="#fff"/></svg>42 Shoreline Rd. Corrabeen 6299</li>
      <li><svg class="icon" viewBox="0 0 12 12"><circle cx="6" cy="6" r="6" fill="var(--blue)"/><rect x="3" y="4" width="6" height="4.2" fill="none" stroke="#fff" stroke-width=".9"/><path d="M3 4l3 2.4L9 4" fill="none" stroke="#fff" stroke-width=".9"/></svg>info@corrabeenholiday.com.au</li>
      <li class="web"><svg class="icon" viewBox="0 0 12 12"><circle cx="6" cy="6" r="6" fill="var(--blue)"/><path d="M2.5 6h7M6 2.5v7" stroke="#fff" stroke-width=".8"/></svg>www.corrabeenholiday.com.au</li>
    </ul>
  </div>

  <div class="panel panel--right bg-cover-right">
    <div class="abs" style="left:0;top:0;width:260px;height:152px;background:linear-gradient(180deg,#3f82c6,#4d8fcf)"></div>
    <div class="abs title" style="left:0;width:260px;top:44px;text-align:center;font-size:34px;color:var(--white)">CORRABEEN</div>
    <div class="abs subtitle" style="left:0;width:260px;top:80px;text-align:center;font-size:15px;color:var(--ink)">HOLIDAY VILLAGE</div>
    <div class="photo" role="img" aria-label="Children jumping from a houseboat into the water" style="left:0;top:152px;width:260px;height:226px;background:linear-gradient(180deg,#bfe2f2 0%,#9fd0ea 40%,#7ab4d6 70%,#6a9ab8 100%)"></div>
    <svg class="abs" style="left:0;top:320px" width="260" height="80" viewBox="0 0 260 80">
      <path d="M0 40 C60 60 150 58 260 30 L260 80 L0 80 Z" fill="#8accea"/>
      <path d="M0 38 C60 58 150 56 260 28" fill="none" stroke="#2f78c0" stroke-width="3"/>
    </svg>
    <ul class="abs contact" style="left:22px;top:486px">
      <li><svg class="icon" viewBox="0 0 12 12"><circle cx="6" cy="6" r="6" fill="var(--blue)"/><path d="M3.6 3.2l1.2-.4.8 1.6-.7.6c.4.9 1 1.5 1.9 1.9l.6-.7 1.6.8-.4 1.2C5.8 8.4 3.6 6.2 3.6 3.2z" fill="#fff"/></svg>(08) 9477 2305</li>
      <li><svg class="icon" viewBox="0 0 12 12"><path d="M6 0.5a4 4 0 0 1 4 4c0 3-4 7-4 7s-4-4-4-7a4 4 0 0 1 4-4z" fill="var(--blue)"/><circle cx="6" cy="4.5" r="1.6" fill="#fff"/></svg>42 Shoreline Rd. Corrabeen 6299</li>
      <li><svg class="icon" viewBox="0 0 12 12"><circle cx="6" cy="6" r="6" fill="var(--blue)"/><rect x="3" y="4" width="6" height="4.2" fill="none" stroke="#fff" stroke-width=".9"/><path d="M3 4l3 2.4L9 4" fill="none" stroke="#fff" stroke-width=".9"/></svg>info@corrabeenholiday.com.au</li>
      <li class="web"><svg class="icon" viewBox="0 0 12 12"><circle cx="6" cy="6" r="6" fill="var(--blue)"/><path d="M2.5 6h7M6 2.5v7" stroke="#fff" stroke-width=".8"/></svg>www.corrabeenholiday.com.au</li>
    </ul>
  </div>
</section>

<section class="spread spread--inside">

  <div class="panel panel--left bg-light">
    <div class="band" style="top:34px">WHAT TO DO?</div>
    <p class="abs sub-head" style="left:31px;top:76px;width:200px">The Estuary is only 2-minutes<br>to the east for:</p>
    <div class="abs pair" style="left:31px;top:116px"><span>Water Sports</span><span>Swimming</span><span>Crabbing</span><span>Prawning</span><span>Boat Ramp Access</span><span>Boating</span></div>
    <span class="abs" style="left:0;top:161px;width:248px;height:2px;background:linear-gradient(90deg,#5cc2da,rgba(92,194,218,.2))"></span>
    <p class="abs sub-head" style="left:31px;top:172px;width:200px">Melrose Beach is 5-minutes<br>to the west for:</p>
    <div class="abs pair" style="left:31px;top:212px"><span>Water Skiing</span><span>Crabbing</span><span>Swimming</span><span>Sailing</span><span>Beach Walking</span><span>Fishing</span><span>Boat Ramp Access</span><span>Surfing</span></div>
    <span class="abs" style="left:0;top:273px;width:248px;height:2px;background:linear-gradient(90deg,#5cc2da,rgba(92,194,218,.2))"></span>
    <p class="abs sub-head" style="left:31px;top:284px">Sporting Facilities 5-minutes</p>
    <div class="abs pair" style="left:99px;top:304px;grid-template-columns:80px"><span>Golfing</span><span>Bowls</span></div>
    <div class="photo" role="img" aria-label="Family crabbing from a wooden jetty" style="left:0;top:318px;width:248px;height:262px;background:linear-gradient(160deg,#9fc7e2 0%,#7ea9c6 45%,#a58f72 100%);clip-path:path('M0 0 C80 40 170 50 248 25 L248 262 L0 262 Z')"></div>
    <svg class="abs" style="left:0;top:306px" width="248" height="70" viewBox="0 0 248 70">
      <path d="M0 12 C80 52 170 62 248 37" fill="none" stroke="#cfe9f5" stroke-width="8"/>
    </svg>
  </div>

  <div class="panel panel--mid bg-light">
    <div class="photo" role="img" aria-label="Sunset over the ocean with people fishing from the shore" style="left:0;top:0;width:264px;height:180px;background:linear-gradient(180deg,#d98a3e 0%,#6a5a63 22%,#2a3f57 40%,#1b2f45 100%);clip-path:path('M0 0 H264 V150 C200 115 110 145 0 180 Z')"></div>
    <svg class="abs" style="left:0;top:110px" width="264" height="80" viewBox="0 0 264 80">
      <path d="M0 68 C100 40 200 20 264 44" fill="none" stroke="#15324f" stroke-width="4"/>
    </svg>
    <div class="band" style="top:194px;width:264px;background:linear-gradient(90deg,#5cc2da 0%,#9adbea 70%,rgba(220,244,250,.3) 100%)">ACCOMODATION</div>
    <ul class="abs plain-list" style="left:27px;top:233px">
      <li>Chalets Ensuite &amp; Air Con</li><li>Caravans</li><li>Caravans Ensuite &amp; Air Con</li><li>Powered SItes</li>
    </ul>
  </div>

  <svg class="abs" style="left:170px;top:336px" width="340" height="244" role="img" aria-label="Dolphin leaping out of the water">
    <defs>
      <linearGradient id="seaFill" x1="0" y1="0" x2="0" y2="1">
        <stop offset="0" stop-color="#9bc57a"/><stop offset=".2" stop-color="#3fb0cf"/><stop offset="1" stop-color="#1f86b8"/>
      </linearGradient>
    </defs>
    <circle cx="170" cy="170" r="160" fill="url(#seaFill)" stroke="#ffffff" stroke-width="4"/>
    <circle cx="170" cy="170" r="164" fill="none" stroke="#5cc2da" stroke-width="3"/>
  </svg>

  <div class="panel panel--right bg-light">
    <div class="band" style="top:22px;width:260px">FACILITIES</div>
    <ul class="abs plain-list" style="left:24px;top:71px">
      <li>EFTPOS</li><li>Swimming Pool</li><li>Undercover BBQ</li><li>Crab Cooker</li>
    </ul>
    <span class="divider" style="left:143px;top:72px;height:88px"></span>
    <ul class="abs plain-list" style="left:161px;top:71px">
      <li>Playground</li><li>Laundrette</li><li>TV Room</li><li>Games Room</li>
    </ul>
    <ul class="abs caps-list" style="left:24px;top:174px">
      <li>2 Supermarkets within 2-minutes</li><li>13 Take-away shops within 7-minutes</li><li>6 Restaurants within 7-minutes</li><li>Mandurah CBO 15-minutes</li>
    </ul>
    <div class="photo" role="img" aria-label="Aerial view of the estuary, canals and bridge" style="left:0;top:268px;width:260px;height:252px;background:linear-gradient(180deg,#2f8fc0 0%,#3b9cc4 35%,#b9b39b 60%,#3e96bd 100%);clip-path:path('M0 50 C60 80 120 70 170 40 C210 18 240 10 260 14 V252 H0 Z')"></div>
    <svg class="abs" style="left:0;top:262px" width="260" height="70" viewBox="0 0 260 70">
      <path d="M0 52 C60 82 120 72 170 42 C210 20 240 12 260 16" fill="none" stroke="#2a6fb4" stroke-width="4"/>
    </svg>
    <div class="abs footer-box">
      <p>For more informations,<br>please contact us or visit our website:</p>
      <div class="footer-line">
        <svg class="icon" style="margin-right:0" viewBox="0 0 12 12"><circle cx="6" cy="6" r="6" fill="var(--blue)"/><path d="M3.6 3.2l1.2-.4.8 1.6-.7.6c.4.9 1 1.5 1.9 1.9l.6-.7 1.6.8-.4 1.2C5.8 8.4 3.6 6.2 3.6 3.2z" fill="#fff"/></svg>
        <span style="margin-right:8px">(08) 9477 2305</span>
        <svg class="icon" style="margin-right:0" viewBox="0 0 12 12"><circle cx="6" cy="6" r="6" fill="var(--blue)"/><path d="M2.5 6h7M6 2.5v7" stroke="#fff" stroke-width=".8"/></svg>
        <span>www.corrabeenholiday.com.au</span>
      </div>
    </div>
  </div>
</section>

</body>
</html>
```